CRM, Marketing Automation for B2B Sales Teams - Home Page

We're repositioning our product and need to redesign our website to match the new messaging and positioning.
Current page - http://www.dealvantor.example
Goal: To emphasize to a new visitor what makes DealVantor unique. Our competitors are brands like pitchmerren.example, https://www.quorvadel.example/en-us/tallix/crm.aspx, Brevantile.example, plovicrm.example and others.
Our main value proposition is that we offer Sales Management, CRM and Marketing Automation all in one easy to set up and use solution.
For a medium sized company with limited IT and marketing resources, this is important. Our competitors offer robust functionality but, only by subscribing to a core platform and then adding on additional products and services. This leaves the customer the challenge of making the pieces work together.
So, we want to emphasize the our solution is all in one. Less time spent setting it up and maintaining it and its easier to use for the team.
We also offer the highest level of service/support in the industry - we help the customer set up their system in the beginning and provide unlimited phone, email and chat support on-going.
Ramp up time is typically 1/2 that of other solutions.
Due to all of the above, customers stay with us 2 times as long as the industry average.
We had some graphics created that attempt to get this message across but, are not happy with them.
The above images are described here not because we have to use them but, just to provide some direction in terms of style and message.
We have also considered that a slider on the home hage with images like growth.jpg could include the key messaging AND screen shots of the application as the image part. Several screen shots are included here.
Our intent is that we'll design the home page and then begin desigining the specific product/feature pages in the same style.
Target Market(s)
B2B Sales Teams from 10 to 200 - mid sized businesses.
Industry/Entity Type
Marketing
Number of Pages Required
1 page
Look and feel
Each slider illustrates characteristics of the customer's brand and the style your logo design should communicate.

```html
<!DOCTYPE html>
<html lang="en">
<head>
<meta charset="utf-8">
<title>DealVantor – Online CRM, Email Marketing and Lead Generation</title>
<link rel="stylesheet" href="https://fonts.googleapis.com/css2?family=Open+Sans:ital,wght@0,300;0,400;0,600;0,700;1,400&display=swap">
<style>
:root{
  --orange:#e8512a;
  --orange-dark:#d9461f;
  --green:#27a744;
  --green-dark:#1d8a36;
  --header:#2e2e2e;
  --hero:#8a8a8a;
  --light:#ececec;
  --text:#555;
  --muted:#777;
  --footer:#3d3d3d;
  --footer-bar:#2a2a2a;
  --white:#fff;
}
*{margin:0;padding:0;box-sizing:border-box}
html,body{width:1200px;height:2253px;overflow:hidden}
body{position:relative;font-family:"Open Sans",Arial,sans-serif;color:var(--text);background:var(--white)}
.abs{position:absolute}

/* header */
.site-header{position:absolute;left:0;top:0;width:1200px;height:96px;background:linear-gradient(#3a3a3a,#262626);border-top:3px solid var(--orange)}
.brand{position:absolute;left:98px;top:24px;font-size:34px;font-weight:700;color:var(--orange);letter-spacing:-1px;line-height:44px}
.main-nav a{position:absolute;top:38px;font-size:13px;color:#eee;text-decoration:none}
.main-nav a.active{color:var(--orange)}

/* hero */
.hero{position:absolute;left:0;top:96px;width:1200px;height:538px;background:linear-gradient(100deg,#5e5e5e 0%,#8f8f8f 45%,#9a9a9a 100%)}
.slider-arrows{position:absolute;left:97px;top:470px}
.solutions-panel{position:absolute;left:813px;top:54px;width:288px;height:430px;background:var(--white);box-shadow:0 3px 12px rgba(0,0,0,.35);text-align:center}
.solutions-panel h2{margin-top:26px;font-size:24px;font-weight:400;color:var(--orange)}
.solutions-panel .sub{font-size:14px;color:#666;margin-top:2px}
.solutions-panel .lead{font-size:11.5px;font-style:italic;color:#888;line-height:22px;padding:10px 22px 0}
.solutions-panel ul{list-style:none;margin-top:12px}
.solutions-panel li{border-top:1px solid #e6e6e6;height:52px;line-height:52px;font-size:17px;color:var(--orange)}
.btn{display:block;position:absolute;height:50px;line-height:50px;text-align:center;color:var(--white);font-size:15px;background:linear-gradient(var(--green),var(--green-dark));border-radius:3px;box-shadow:0 2px 3px rgba(0,0,0,.25);text-decoration:none}
.solutions-panel .btn{left:44px;top:357px;width:200px;border-top:1px solid #e6e6e6}

/* features */
.features{position:absolute;left:0;top:634px;width:1200px;height:526px;background:var(--light);text-align:center}
.features h1{margin-top:34px;font-size:27px;font-weight:400;color:var(--orange)}
.features .intro{margin:8px auto 0;width:600px;font-size:14px;line-height:22px;color:#555}
.feature-card{position:absolute;top:224px;width:300px;height:247px;background:var(--white);border-top:3px solid var(--orange);box-shadow:0 8px 8px -6px rgba(0,0,0,.25)}
.feature-icon{position:absolute;left:88px;top:-71px;width:124px;height:124px;border-radius:50%;background:var(--orange);border:4px solid #ef7a57;display:flex;align-items:center;justify-content:center}
.feature-card h3{margin-top:68px;font-size:14px;font-weight:400;color:var(--orange)}
.feature-card .role{font-size:12px;font-style:italic;color:#555;margin-top:2px}
.feature-card p{font-size:11.5px;line-height:22px;color:#666;padding:8px 22px 0}

/* implementation */
.implementation{position:absolute;left:0;top:1160px;width:1200px;height:360px;overflow:hidden}
.impl-copy{position:absolute;left:96px;top:36px;width:292px;color:var(--white)}
.impl-copy h2{font-size:44px;font-weight:300;line-height:50px}
.impl-copy .sub{font-size:17px;margin-top:2px;padding-bottom:12px;border-bottom:1px solid rgba(255,255,255,.7);width:272px}
.impl-copy .quote{font-size:24px;margin-top:10px;white-space:nowrap;line-height:34px}
.impl-copy p{font-size:13.5px;font-style:italic;line-height:25px;margin-top:6px}
.help-piece{position:absolute;top:1244px;width:193px;height:200px;text-align:center;font-size:17px;padding-top:54px}
.help-piece.light{background:var(--white);color:var(--orange)}
.help-piece.accent{background:var(--orange);color:var(--white)}
.help-piece svg{display:block;margin:18px auto 0}

/* growth */
.growth{position:absolute;left:0;top:1520px;width:1200px;height:395px;background:var(--white)}
.growth-visual{position:absolute;left:112px;top:48px;width:340px;height:300px;background:linear-gradient(135deg,#dfe9f1,#a9bccc);border:14px solid #222;border-radius:6px}
.growth-base{position:absolute;left:100px;top:373px;width:355px;height:22px;background:var(--green)}
.growth-copy{position:absolute;left:540px;top:60px;width:565px}
.growth-copy h2{font-size:44px;font-weight:300;color:var(--green);line-height:50px}
.growth-copy .sub{font-size:19px;color:#555;margin-top:2px}
.growth-copy p{font-size:11.5px;line-height:23px;color:#666;margin-top:10px}
.growth .btn{left:540px;top:282px;width:200px}

/* footer */
.site-footer{position:absolute;left:0;top:1915px;width:1200px;height:283px;background:var(--footer);border-top:3px solid var(--green);color:#ddd}
.footer-col{position:absolute;top:58px}
.footer-col h4{font-size:16px;font-weight:400;color:#eee;margin-bottom:10px}
.footer-col ul{list-style:none}
.footer-col li{font-size:11.5px;line-height:26px;padding-left:12px;position:relative}
.footer-col li::before{content:"";position:absolute;left:0;top:11px;width:5px;height:5px;border-radius:50%;background:#eee}
.footer-col.social li{padding-left:22px}
.footer-col.social li::before{left:0;top:7px;width:12px;height:12px;border-radius:2px}
.partner-badge{position:absolute;width:87px;height:40px;background:#1f5a7a;border:2px solid #eee}
.partner-badge.dark{background:#1a1a1a}
.partner-badge.light{background:#fafafa}
.footer-bar{position:absolute;left:0;top:2198px;width:1200px;height:55px;background:var(--footer-bar);text-align:center;line-height:55px;font-size:11.5px;color:#ddd}
</style>
</head>
<body>

<header class="site-header">
  <div class="brand">dealvantor</div>
  <nav class="main-nav">
    <a class="active" style="left:450px">Home</a>
    <a style="left:541px">Online CRM</a>
    <a style="left:662px">Email Marketing</a>
    <a style="left:808px">Lead Generation</a>
    <a style="left:958px">Pricing</a>
    <a style="left:1075px">Learning</a>
  </nav>
</header>

<section class="hero" role="img" aria-label="Photo of a hand holding a magnifying glass over a crowd of small customer figures">
  <svg class="slider-arrows" width="34" height="36" viewBox="0 0 34 36" fill="none" stroke="#eee" stroke-width="2">
    <polyline points="13,3 3,18 13,33"/><polyline points="21,3 31,18 21,33"/>
  </svg>
  <aside class="solutions-panel">
    <h2>CUSTOM SOLUTIONS</h2>
    <div class="sub">Without the Custom Price</div>
    <p class="lead">Lorem ipsum dolor sit amet, cadipiscing elit, sed veniam, quis nostrud exercitation ullamco Duis velit esse cillum dolore eu fugiat...</p>
    <ul>
      <li>Sales Enablement</li>
      <li>Lead Nurturing &amp; Generation</li>
      <li>Process Automation</li>
      <li></li>
    </ul>
    <a class="btn">Try Us Free For 30 days!</a>
  </aside>
</section>

<section class="features">
  <h1>Online CRM Software, Email Marketing, and Lead Generation</h1>
  <p class="intro">The best online CRM software and email marketing software rolled into one platform to help you reach and manage your customers.</p>

  <article class="feature-card" style="left:98px">
    <div class="feature-icon">
      <svg width="46" height="46" viewBox="0 0 46 46" fill="none" stroke="#fff" stroke-width="4"><circle cx="23" cy="23" r="19"/><circle cx="23" cy="23" r="10"/><circle cx="23" cy="23" r="2" fill="#fff"/></svg>
    </div>
    <h3>TARGET</h3>
    <div class="role">Lead Generation</div>
    <p>Sometimes finding new leads is the hardest part. Download 500 leads each month from LeadQuarry.example straight into our sales crm software to give you more time to connect and convert with your best leads...</p>
  </article>

  <article class="feature-card" style="left:450px">
    <div class="feature-icon">
      <svg width="46" height="34" viewBox="0 0 46 34"><rect x="0" y="0" width="46" height="34" rx="3" fill="#fff"/><polyline points="3,4 23,19 43,4" fill="none" stroke="#e8512a" stroke-width="3"/></svg>
    </div>
    <h3>CONNECT</h3>
    <div class="role">Email Marketing</div>
    <p>Sometimes finding new leads is the hardest part. Download 500 leads each month from LeadQuarry.example straight into our sales crm software to give you more time to connect and convert with your best leads...</p>
  </article>

  <article class="feature-card" style="left:801px">
    <div class="feature-icon">
      <svg width="44" height="44" viewBox="0 0 44 44" fill="none" stroke="#fff" stroke-width="5"><path d="M36 16 A15 15 0 0 0 8 16"/><path d="M8 28 A15 15 0 0 0 36 28"/><polygon points="38,6 38,19 26,17" fill="#fff" stroke="none"/><polygon points="6,38 6,25 18,27" fill="#fff" stroke="none"/></svg>
    </div>
    <h3>CONVERT</h3>
    <div class="role">Online CRM Software</div>
    <p>Sometimes finding new leads is the hardest part. Download 500 leads each month from LeadQuarry.example straight into our sales crm software to give you more time to connect and convert with your best leads...</p>
  </article>
</section>

<section class="implementation">
  <svg class="abs" style="left:0;top:0" width="1200" height="360" viewBox="0 0 1200 360">
    <defs><linearGradient id="darkOffice" x1="0" y1="0" x2="1" y2="1"><stop offset="0" stop-color="#2b3036"/><stop offset="1" stop-color="#14171b"/></linearGradient></defs>
    <rect width="1200" height="360" fill="url(#darkOffice)" role="img" aria-label="Dark office backdrop with faint business diagrams"/>
    <path d="M0 0 H520 C440 60 395 220 420 360 H0 Z" fill="#5a5a5a"/>
    <path d="M0 0 H505 C425 60 380 220 405 360 H0 Z" fill="var(--orange)"/>
  </svg>
  <div class="impl-copy">
    <h2>PAIN FREE</h2>
    <div class="sub">Implimentation Services</div>
    <div class="quote">"Fastest Ramp up Time"</div>
    <p>Sed quia consequuntur magni dolores eos qui porro quisquam est, qui dolorem ipsum quia quia non numquam abore et dolore magnam minima veniam, quis nostrum exercitationem ullam corporis eius modi tempora...</p>
  </div>
</section>

<div class="help-piece light" style="left:522px">WEBINAR
  <svg width="30" height="28" viewBox="0 0 30 28"><rect x="0" y="0" width="30" height="20" rx="2" fill="#e8512a"/><rect x="3" y="3" width="24" height="14" fill="#fff"/><rect x="11" y="20" width="8" height="5" fill="#e8512a"/><rect x="7" y="25" width="16" height="3" fill="#e8512a"/></svg>
</div>
<div class="help-piece accent" style="left:715px">NEED HELP?
  <svg width="30" height="30" viewBox="0 0 30 30"><path d="M4 26 L17 13" stroke="#fff" stroke-width="5" stroke-linecap="round"/><circle cx="21" cy="9" r="7" fill="#fff"/><circle cx="24" cy="6" r="3.5" fill="#e8512a"/></svg>
</div>
<div class="help-piece light" style="left:908px">SAY HELLO
  <svg width="34" height="28" viewBox="0 0 34 28"><ellipse cx="13" cy="11" rx="13" ry="10" fill="#e8512a"/><polygon points="5,18 3,26 12,20" fill="#e8512a"/><ellipse cx="23" cy="16" rx="11" ry="8" fill="#e8512a" stroke="#fff" stroke-width="2"/></svg>
</div>

<section class="growth">
  <div class="growth-visual" role="img" aria-label="Computer monitor showing a hand pointing at charts on a tablet"></div>
  <div class="growth-base"></div>
  <div class="growth-copy">
    <h2>GROWTH</h2>
    <div class="sub">More Than Technology, A Partner in Your</div>
    <p>Sed ut perspiciatis unde omnis iste natus error sit voluptatem accusantium doloremque laudantium, totam cabo. Nemo enim ipsam voluptatem quia voluptas sit aspernatur aut odit aut fugit, sed quia consequuntur quia dolor sit amet, consectetur, adipisci velit, sed quia non numquam eius modi tempora incidunt ut labore et dolore magnam aliquam quaerat voluptatem. Ut enim ad minima veniam, quis nostrum exercitationem ullam corporis suscipit laboriosam, reprehenderit qui in ea voluptate velit esse...</p>
  </div>
  <a class="btn">Click to View More</a>
</section>

<footer class="site-footer">
  <div class="footer-col" style="left:98px"><h4>Welcome</h4>
    <ul><li>Home</li><li>Online CRM</li><li>Email Marketing</li><li>Lead Generation</li><li>Pricing</li><li>Orange Peel</li></ul></div>
  <div class="footer-col" style="left:290px"><h4>Quick Links</h4>
    <ul><li>Quickstart</li><li>Customers</li><li>About Us</li><li>Blog</li><li>FAQ</li></ul></div>
  <div class="footer-col" style="left:480px"><h4>Information</h4>
    <ul><li>Compare Us</li><li>Support</li><li>Affiliate</li><li>API</li><li>Privacy, Security and Returns</li></ul></div>
  <div class="footer-col" style="left:738px"><h4>Support</h4></div>
  <div class="partner-badge" style="left:738px;top:99px"></div>
  <div class="partner-badge dark" style="left:837px;top:99px"></div>
  <div class="partner-badge light" style="left:738px;top:151px"></div>
  <div class="partner-badge light" style="left:837px;top:151px"></div>
  <div class="footer-col social" style="left:1020px"><h4>Follow Us</h4>
    <ul><li>Friendwall</li><li>Chirper</li><li>Circlespace</li><li>Pinboardly</li><li>Worklink</li></ul></div>
</footer>
<div class="footer-bar">Copy rights © dealvantor .2015 | Allrights Reserved</div>

</body>
</html>
```